DELCOUR ROOFING YARD SIGN

We need a yard sign to put in our customers' yards when we are roofing their home.
Delcour Roofing
438 Fenwick Rd
Lake Charles LA 70615
phone: 337-555-0142

Maybe some verbiage like "Your Hometown Roofing Experts"
or
"Family Owned Since 1956"

```html
<!DOCTYPE html>
<html lang="en">
<head>
<meta charset="utf-8">
<title>Delcour Roofing Yard Sign</title>
<link rel="stylesheet" href="https://fonts.googleapis.com/css2?family=Rozha+One&family=Alegreya+Sans:wght@500&family=Marcellus&display=swap">
<style>
  :root {
    --page: #3a3a3a;
    --black: #0c0c0c;
    --charcoal: #2b2b2b;
    --steel: #8a8a8a;
    --silver: #c9c9c9;
    --white: #ffffff;
    --ink: #111111;
    --sky: #b9c4cc;
    --tile: #c8653f;
  }
  html, body {
    margin: 0;
    width: 1200px;
    height: 1174px;
    overflow: hidden;
    background: radial-gradient(ellipse at 60% 50%, #5a5a5a 0%, var(--page) 70%);
  }
  .sign {
    position: absolute;
    left: 40px;
    top: 423px;
    width: 1120px;
    height: 328px;
    overflow: hidden;
    box-shadow: 0 14px 30px rgba(0,0,0,0.55);
  }
  .sign__art { position: absolute; inset: 0; }
  .brand-name {
    position: absolute;
    left: 24px;
    top: 6px;
    margin: 0;
    font-family: "Rozha One", serif;
    font-weight: 400;
    font-size: 86px;
    line-height: 74px;
    letter-spacing: 2px;
    color: var(--white);
  }
  .tagline {
    position: absolute;
    left: 26px;
    top: 188px;
    margin: 0;
    font-family: "Alegreya Sans", sans-serif;
    font-weight: 500;
    font-size: 38px;
    line-height: 52px;
    color: var(--white);
  }
  .contact {
    position: absolute;
    left: 30px;
    top: 268px;
    width: 520px;
    margin: 0;
    font-family: "Marcellus", serif;
    font-size: 24px;
    line-height: 27px;
    color: var(--ink);
    text-align: center;
  }
  .contact span { display: block; }
  .seal {
    position: absolute;
    left: 498px;
    top: 16px;
    width: 142px;
    height: 142px;
    display: flex;
    align-items: center;
    justify-content: center;
    text-align: center;
    font-family: "Marcellus", serif;
    font-size: 17px;
    line-height: 20px;
    color: var(--ink);
  }
</style>
</head>
<body>
  <div class="sign">
    <svg class="sign__art" width="1120" height="328" viewBox="0 0 1120 328">
      <defs>
        <linearGradient id="darkPanel" x1="0" y1="0" x2="1" y2="0.3">
          <stop offset="0" stop-color="#050505"/>
          <stop offset="0.55" stop-color="#1c1c1c"/>
          <stop offset="1" stop-color="#3b3b3b"/>
        </linearGradient>
        <linearGradient id="roofScene" x1="0" y1="0" x2="0.2" y2="1">
          <stop offset="0" stop-color="var(--sky)"/>
          <stop offset="0.3" stop-color="#c4ad9c"/>
          <stop offset="0.6" stop-color="var(--tile)"/>
          <stop offset="1" stop-color="#a9553a"/>
        </linearGradient>
        <linearGradient id="crewA" x1="0" y1="0" x2="1" y2="1">
          <stop offset="0" stop-color="#c9d3dc"/>
          <stop offset="0.5" stop-color="#e0642a"/>
          <stop offset="1" stop-color="#4d5a78"/>
        </linearGradient>
        <linearGradient id="crewB" x1="0" y1="0" x2="0.6" y2="1">
          <stop offset="0" stop-color="#d9dde2"/>
          <stop offset="0.5" stop-color="#8c96a3"/>
          <stop offset="1" stop-color="#3e4c66"/>
        </linearGradient>
        <linearGradient id="addressBand" x1="0" y1="0" x2="1" y2="0">
          <stop offset="0" stop-color="#ffffff"/>
          <stop offset="0.6" stop-color="#e6e6e6"/>
          <stop offset="1" stop-color="#9a9a9a"/>
        </linearGradient>
        <radialGradient id="sealFace" cx="0.45" cy="0.4" r="0.65">
          <stop offset="0" stop-color="#ffffff"/>
          <stop offset="1" stop-color="#d4d4d4"/>
        </radialGradient>
      </defs>

      <rect class="panel-dark" width="1120" height="328" fill="url(#darkPanel)"/>

      <rect class="photo-main" x="560" y="0" width="560" height="328" fill="url(#roofScene)" role="img" aria-label="Photo of a roofer in a green sweater and cap laying orange clay roof tiles"/>

      <circle class="arc-outer" cx="650" cy="90" r="232" fill="var(--silver)"/>
      <circle class="arc-white" cx="650" cy="90" r="222" fill="var(--white)"/>
      <circle class="arc-inner" cx="650" cy="90" r="210" fill="url(#darkPanel)"/>
      <rect x="0" y="-20" width="560" height="360" fill="url(#darkPanel)"/>

      <rect class="rule" x="0" y="178" width="660" height="4" fill="var(--steel)"/>
      <rect class="tagline-band" x="0" y="185" width="640" height="56" fill="var(--black)"/>
      <rect class="rule" x="0" y="244" width="680" height="4" fill="var(--steel)"/>
      <rect class="address-band" x="0" y="264" width="720" height="64" fill="url(#addressBand)"/>

      <circle class="seal-ring" cx="569" cy="87" r="73" fill="var(--silver)"/>
      <circle class="seal-face" cx="569" cy="87" r="68" fill="url(#sealFace)"/>

      <circle cx="722" cy="211" r="85" fill="var(--white)"/>
      <circle class="photo-small" cx="722" cy="211" r="76" fill="url(#crewA)" role="img" aria-label="Photo of a roofer in an orange safety vest and yellow hard hat fastening metal roofing"/>

      <circle cx="986" cy="226" r="124" fill="var(--white)"/>
      <circle class="photo-large" cx="986" cy="226" r="114" fill="url(#crewB)" role="img" aria-label="Photo of two roofers in hard hats nailing asphalt shingles"/>
    </svg>

    <h1 class="brand-name">DELCOUR<br>ROOFING</h1>
    <div class="seal">Delcour<br>Roofing</div>
    <p class="tagline">Your Hometown Roofing Experts</p>
    <p class="contact">
      <span>438 Fenwick Rd, Lake Charles LA 70615</span>
      <span>Phone: 337-555-0142</span>
    </p>
  </div>
</body>
</html>
```